Business Card Design - Crisp & Clean

Looking for a new clean and crisp business card design. Design must incorporate our corporate colors (see attached style sheet). We're a pretty fun loving group who likes to keep it light while still portraying a professional image. Card should incorporate both our logo and our mascot (see attachment). Card should be double sided and should have room for our social media - Gleamrow, Brisk Hub and Zumbly on the back. Font selections do not have to match the style guide.

```html
<!DOCTYPE html>
<html lang="en">
<head>
<meta charset="utf-8">
<title>LumoraHR Business Card</title>
<link href="https://fonts.googleapis.com/css2?family=Open+Sans:ital,wght@0,400;0,600;0,700;1,600&family=Arimo:wght@400;700&display=swap" rel="stylesheet">
<style>
  :root {
    --backdrop: #cfcfcb;
    --card: #ffffff;
    --brand-yellow: #f2b21f;
    --ink: #1d1d1d;
    --mascot-light: #eeedea;
    --mascot-mid: #d6d2cd;
  }
  html, body {
    margin: 0;
    padding: 0;
    width: 1200px;
    height: 1200px;
    overflow: hidden;
    background: var(--backdrop);
  }
  .canvas {
    position: relative;
    width: 1200px;
    height: 1200px;
  }
  .card {
    position: absolute;
    background: var(--card);
    overflow: hidden;
  }
  .card--front { left: 45px; top: 40px; width: 1008px; height: 505px; }
  .card--back  { left: 147px; top: 657px; width: 1019px; height: 510px; }

  .brand {
    position: absolute;
    display: flex;
    align-items: center;
    gap: 14px;
    font-family: "Arimo", Arial, sans-serif;
    font-weight: 700;
    color: var(--ink);
    letter-spacing: 0.5px;
  }
  .brand__dot {
    width: 54px;
    height: 54px;
    border-radius: 50%;
    background: var(--brand-yellow);
  }
  .brand__name { font-size: 44px; }

  .front__accent-left {
    position: absolute; left: 0; top: 12px; width: 53px; height: 76px;
    background: var(--brand-yellow);
  }
  .front__accent-right {
    position: absolute; left: 447px; top: 17px; width: 561px; height: 72px;
    background: var(--brand-yellow);
  }
  .card--front .brand { left: 78px; top: 26px; }

  .mascot {
    position: absolute;
    border-radius: 24px;
    background: linear-gradient(180deg, var(--mascot-light) 0%, var(--mascot-mid) 100%);
  }
  .card--front .mascot { left: 35px; top: 155px; width: 175px; height: 323px; }
  .card--back .mascot  { left: 533px; top: 55px; width: 318px; height: 435px; }

  .contact {
    position: absolute;
    left: 498px;
    top: 125px;
    font-family: "Open Sans", Arial, sans-serif;
    color: var(--ink);
  }
  .contact__name {
    margin: 0;
    font-size: 30px;
    font-weight: 700;
    letter-spacing: 1px;
  }
  .contact__role {
    margin: 8px 0 0 33px;
    font-size: 22px;
    font-weight: 700;
  }
  .contact__company {
    margin: 24px 0 0 -3px;
    font-size: 29px;
    font-weight: 600;
    font-style: italic;
    color: var(--brand-yellow);
  }
  .contact__line {
    display: flex;
    align-items: center;
    gap: 10px;
    margin: 24px 0 0 15px;
    font-family: "Arimo", Arial, sans-serif;
    font-size: 28px;
  }
  .contact__line + .contact__line { margin-top: 22px; }
  .contact__line svg { flex: none; }

  .card--back .brand { left: 71px; top: 48px; }
  .social {
    position: absolute;
    left: 0; top: 213px;
    width: 425px; height: 192px;
    background: var(--brand-yellow);
    font-family: "Arimo", Arial, sans-serif;
    color: var(--ink);
  }
  .social__title {
    margin: 10px 0 0 18px;
    font-size: 27px;
  }
  .social__list {
    list-style: none;
    margin: 10px 0 0 64px;
    padding: 0;
    font-size: 26px;
    font-weight: 700;
    line-height: 48px;
  }
</style>
</head>
<body>
<main class="canvas">

  <section class="card card--front" aria-label="Card front">
    <div class="front__accent-left"></div>
    <div class="front__accent-right"></div>
    <div class="brand">
      <span class="brand__dot"></span>
      <span class="brand__name">LumoraHR</span>
    </div>
    <div class="mascot" role="img" aria-label="Company mascot illustration"></div>

    <div class="contact">
      <h1 class="contact__name">DANA WHITFIELD</h1>
      <p class="contact__role">Marketing Wizard</p>
      <p class="contact__company">LumoraHR Processing Solutions</p>
      <p class="contact__line">
        <svg width="32" height="32" viewBox="0 0 24 24" aria-hidden="true"><path fill="none" stroke="#f2b21f" stroke-width="2.6" d="M16 12a4 4 0 1 1-1.2-2.9V13a2.5 2.5 0 0 0 5 0v-1a8 8 0 1 0-3 6.3"/></svg>
        dana@lumorahr.com
      </p>
      <p class="contact__line">
        <svg width="32" height="32" viewBox="0 0 24 24" aria-hidden="true"><rect x="6" y="2" width="12" height="20" rx="2" fill="none" stroke="#f2b21f" stroke-width="2"/><line x1="10" y1="18.5" x2="14" y2="18.5" stroke="#f2b21f" stroke-width="1.6"/></svg>
        555-010-2748
      </p>
    </div>
  </section>

  <section class="card card--back" aria-label="Card back">
    <div class="brand">
      <span class="brand__dot"></span>
      <span class="brand__name">LumoraHR</span>
    </div>
    <div class="social">
      <p class="social__title">Follow us on</p>
      <ul class="social__list">
        <li>Gleamrow</li>
        <li>Brisk Hub</li>
        <li>Zumbly</li>
      </ul>
    </div>
    <div class="mascot" role="img" aria-label="Company mascot illustration"></div>
  </section>

</main>
</body>
</html>
```